I am a surgeon that operates on gynaecological cancer. Wish a design and logo for letter head.

Design should include my name: Dr. Torin Halwell, qualifications: FKMLTPVB, DMR. and state that I am a Gynaecological Oncologist and Advanced Laparoscopic Surgeon.
As for a logo. As all cancer is related to DNA, I think that that double helix could be used to symbolise a female shape, exaggerating the abdomen to suggest a mass.

Reason: Extended to view changes I have asked for.

```html
<!DOCTYPE html>
<html lang="en">
<head>
<meta charset="utf-8">
<title>Dr. Torin Halwell – Letterhead</title>
<link rel="stylesheet" href="https://fonts.googleapis.com/css2?family=Alegreya+Sans:wght@400;500;700&display=swap">
<style>
  :root {
    --bg: #e9edef;
    --paper: #ffffff;
    --green: #3aaa35;
    --orange: #f7941d;
    --grey: #5a5a5a;
    --rule: #7cc576;
  }
  * { margin: 0; padding: 0; box-sizing: border-box; }
  html, body { width: 1000px; height: 1200px; overflow: hidden; }
  body {
    position: relative;
    background: var(--bg);
    font-family: "Alegreya Sans", "Helvetica Neue", Arial, sans-serif;
  }
  .letterhead {
    position: absolute;
    left: 176px; top: 80px;
    width: 742px; height: 720px;
    background: var(--paper);
  }
  .letterhead__mark {
    position: absolute;
    left: 46px; top: 40px;
    width: 38px; height: 38px;
    border-radius: 50%;
    background: var(--orange);
  }
  .letterhead__text {
    position: absolute;
    left: 100px; top: 70px;
    line-height: 1;
  }
  .letterhead__name {
    color: var(--green);
    font-weight: 700;
    font-size: 16px;
    margin-bottom: 1px;
  }
  .letterhead__credentials,
  .letterhead__title {
    color: var(--grey);
    font-size: 12px;
    line-height: 13px;
  }
  .letterhead__rule {
    position: absolute;
    left: 46px; top: 121px;
    width: 664px; height: 1px;
    background: var(--rule);
  }
  .letterhead__rule::after {
    content: "";
    position: absolute;
    right: -3px; top: -2.5px;
    width: 6px; height: 6px;
    border-radius: 50%;
    background: var(--orange);
  }
  .lockup {
    position: absolute;
    left: 160px; top: 915px;
  }
  .lockup__mark {
    position: absolute;
    left: 14px; top: 30px;
    width: 72px; height: 72px;
    border-radius: 50%;
    background: var(--orange);
  }
  .lockup__text {
    position: absolute;
    left: 102px; top: 64px;
    white-space: nowrap;
  }
  .lockup__name {
    color: var(--green);
    font-weight: 700;
    font-size: 30px;
    line-height: 34px;
  }
  .lockup__credentials,
  .lockup__title {
    color: var(--grey);
    font-size: 23px;
    line-height: 26px;
  }
</style>
</head>
<body>
  <section class="letterhead">
    <div class="letterhead__mark" aria-hidden="true"></div>
    <div class="letterhead__text">
      <p class="letterhead__name">Dr. Torin Halwell</p>
      <p class="letterhead__credentials">FKMLTPVB, DMR</p>
      <p class="letterhead__title">Gynaecological Oncologist and Advanced Laparoscopic Surgeon</p>
    </div>
    <div class="letterhead__rule"></div>
  </section>

  <section class="lockup">
    <div class="lockup__mark" aria-hidden="true"></div>
    <div class="lockup__text">
      <p class="lockup__name">Dr. Torin Halwell</p>
      <p class="lockup__credentials">FKMLTPVB, DMR</p>
      <p class="lockup__title">Gynaecological Oncologist and Advanced Laparoscopic Surgeon</p>
    </div>
  </section>
</body>
</html>
```